依頼詳細

■デザインイメージ
─────────────────────────────────────

1.添付のPPTファイルを参考に、ご提案を1枚作成いただきたいです。
2.デザイン上、文字や図の配置は素案から変更していただいて一向に結構ですが、
タイトルの文字の大きさや位置(一番上)は、10m先からタイトル文字が見えるようにし
たいので、それが適う範囲でデザインをお願いします。
3.セキュリティ製品を取り扱っているので、セキュリティをイメージできるもの。
4.製品マーク(盾)は必ず使用してください。
5.提案いただいたデザインと類似デザインで、残りの2~3枚をご制作いただく想定です。

■ 入稿詳細
作成ファイル :イラストレータファイル(EPS)
Illustrator CS5まで
サイズ : A1(パネル 594 × 841mm)
記載項目
添付のPPTをご参照ください。
希望イメージ
シンプル 複雑
単色 カラフル
暗い 明るい
日常 高級
遊び心 厳粛
未来的 伝統的
女性的 男性的
希望する色
緑・黒を基調としたもの
納品ファイル
• イラストレーター形式 (.ai)
補足説明

※9月30日にはパネル制作へ入稿を予定、
コンペ(1枚目)・プロジェクト(2~3枚)共にご対応いただける方を希望します。

以上となります。
宜しくお願い致します。
提案予約をいただいている方が、複数名いらっしゃいますので、
1日締め切りを延ばさせていただきます。
■ 選んだ理由

固いイメージを保ちつつ、シンプルな印象で
あまり、懲りすぎていないデザインがよかったため、
こちらのデザインを選定させていただきました。

また、緑色を多用しすぎていないところも気に入りました。

■ 提案者全員のお礼・コメント

どの方のデザインもとても素敵で、
選定に悩みました。

たくさんのデザインをご提案いただき、
誠に有難う御座いました。

```html
<!DOCTYPE html>
<html lang="ja">
<head>
<meta charset="utf-8">
<title>操作制御 ログ取得</title>
<link rel="stylesheet" href="https://fonts.googleapis.com/css2?family=Noto+Sans+JP:wght@400;700;900&display=swap">
<style>
:root{
  --black:#050805;
  --green:#7ec234;
  --green-bright:#a6e03c;
  --green-deep:#2f6a12;
  --white:#ffffff;
  --red:#d6141c;
  --tag-server:#8ccf2e;
  --tag-pc:#9b59c9;
  --tag-db:#f2d229;
  --tag-prog:#e8559b;
  --tag-net:#2fb7e8;
  --text-soft:#dfe8d6;
}
*{margin:0;padding:0;box-sizing:border-box}
html,body{width:849px;height:1200px;overflow:hidden;background:var(--black)}
body{font-family:"Noto Sans JP",sans-serif;color:var(--white)}
.poster{position:relative;width:849px;height:1200px;overflow:hidden;background:var(--black)}
.code-rain{position:absolute;inset:0;background:
  radial-gradient(ellipse at 50% 60%,rgba(60,140,40,.35),transparent 70%),
  linear-gradient(180deg,#071207 0%,#0c1f0b 50%,#061006 100%)}
.content-panel{position:absolute;left:40px;top:368px;width:769px;height:817px;background:rgba(70,85,65,.55)}
.brand{position:absolute;left:22px;top:28px;display:flex;flex-direction:column;align-items:center;gap:8px;width:70px}
.brand-square{width:56px;height:56px;background:var(--green)}
.brand-name{font-weight:900;font-size:14px;color:var(--green);letter-spacing:.02em}
.title{font-weight:900;color:var(--green);-webkit-text-stroke:4px var(--white);paint-order:stroke fill}
.title-line{position:absolute;display:block;white-space:nowrap;line-height:1;letter-spacing:0}
.title-line-1{left:212px;top:12px;font-size:150px}
.title-line-2{left:248px;top:180px;font-size:144px}
.tags{position:absolute;left:90px;top:192px;list-style:none;display:flex;flex-direction:column;gap:4px}
.tags li{width:150px;height:30px;line-height:30px;padding-left:10px;font-weight:700;font-size:17px;color:var(--white)}
.tag-server{background:var(--tag-server)}.tag-pc{background:var(--tag-pc)}.tag-db{background:var(--tag-db)}
.tag-prog{background:var(--tag-prog)}.tag-net{background:var(--tag-net)}
.lead{position:absolute;left:90px;top:380px}
.lead-sub{font-weight:900;font-size:21px}
.lead-main{margin-top:6px;display:inline-block;background:var(--green);color:var(--white);font-weight:900;font-size:34px;padding:0 10px;line-height:46px}
.intro{position:absolute;left:418px;top:382px;width:395px}
.intro-head{font-weight:900;font-size:18px;line-height:26px;white-space:nowrap}
.intro-body{margin-top:6px;font-size:10.5px;line-height:16px;color:var(--text-soft)}
.diagram{position:absolute;left:0;top:500px}
.diagram text{font-family:"Noto Sans JP",sans-serif}
</style>
</head>
<body>
<main class="poster">
  <div class="code-rain" role="img" aria-label="緑色の文字が流れるデジタルコードの背景パターン"></div>
  <div class="content-panel"></div>

  <div class="brand"><span class="brand-square"></span><span class="brand-name">SENTRA</span></div>

  <h1 class="title"><span class="title-line title-line-1">操作制御</span><span class="title-line title-line-2">ログ取得</span></h1>

  <ul class="tags">
    <li class="tag-server">サーバー</li>
    <li class="tag-pc">パソコン</li>
    <li class="tag-db">データベース</li>
    <li class="tag-prog">プログラム</li>
    <li class="tag-net">ネットワーク</li>
  </ul>

  <div class="lead">
    <p class="lead-sub">簡単、安全、そして確実に</p>
    <p class="lead-main">自動監査システム</p>
  </div>

  <div class="intro">
    <p class="intro-head">エージェントによる徹底した操作制御とログ取得</p>
    <p class="intro-body">各プラットフォームのコンピュータに対応し、操作を確実に記録します。導入は簡単で既存環境をそのまま活かせます。SENTRA Trace Agentを導入するだけで、端末やサーバーの操作・通信・稼働状況を詳細に取得し、社内のセキュリティ対策を強化します。</p>
  </div>

  <svg class="diagram" width="849" height="700" viewBox="0 500 849 700" xmlns="http://www.w3.org/2000/svg">
    <defs>
      <radialGradient id="pill" cx="50%" cy="35%" r="60%">
        <stop offset="0" stop-color="#b8ec4a"/><stop offset="1" stop-color="#5ea322"/>
      </radialGradient>
      <linearGradient id="cyl" x1="0" x2="1">
        <stop offset="0" stop-color="#3f8f1c"/><stop offset=".5" stop-color="#9ad83c"/><stop offset="1" stop-color="#3f8f1c"/>
      </linearGradient>
    </defs>

    <g font-weight="900" font-size="15" fill="#fff" text-anchor="middle">
      <ellipse cx="185" cy="567" rx="86" ry="52" fill="url(#pill)"/>
      <text x="185" y="562">コンピュータ操作制御</text><text x="185" y="583">ログ取得</text>
      <ellipse cx="355" cy="567" rx="86" ry="52" fill="url(#pill)"/>
      <text x="355" y="562">データベース</text><text x="355" y="583">アクセスログ取得</text>
      <ellipse cx="525" cy="567" rx="86" ry="52" fill="url(#pill)"/>
      <text x="525" y="562">プログラム変更</text><text x="525" y="583">ログ取得</text>
      <ellipse cx="698" cy="567" rx="86" ry="52" fill="url(#pill)"/>
      <text x="698" y="562">マルウェア</text><text x="698" y="583">Web改ざん検知</text>

      <ellipse cx="185" cy="703" rx="86" ry="52" fill="url(#pill)"/>
      <text x="185" y="698">ファイルサーバー</text><text x="185" y="719">アクセスログ取得</text>
      <ellipse cx="355" cy="703" rx="86" ry="52" fill="url(#pill)"/>
      <text x="355" y="698">ネットワーク</text><text x="355" y="719">パケット取得</text>
      <ellipse cx="525" cy="703" rx="86" ry="52" fill="url(#pill)"/>
      <text x="525" y="698">サーバー稼働</text><text x="525" y="719">イベントログ取得</text>
      <ellipse cx="698" cy="703" rx="86" ry="52" fill="url(#pill)"/>
      <text x="698" y="698">CPU,メモリ,HDD</text><text x="698" y="719">使用量取得</text>
    </g>

    <path d="M110 765 L740 765 L470 815 L470 838 L380 838 L380 815 Z" fill="#6fb52a" opacity=".85"/>

    <rect x="110" y="840" width="630" height="30" fill="#7ec234"/>
    <text x="425" y="862" text-anchor="middle" font-weight="900" font-size="17" fill="#fff">統合ログ管理マネージャによるログ一元化と自動監査システム</text>
    <text x="425" y="887" text-anchor="middle" font-size="10.5" fill="#dfe8d6">SENTRA Trace Managerが全てのログを集約し、ポリシーに基づき自動で監査します。</text>
    <text x="425" y="903" text-anchor="middle" font-size="10.5" fill="#dfe8d6">違反を検知すると管理者と操作者へ即座に警告を通知します。</text>

    <ellipse cx="226" cy="1025" rx="98" ry="18" fill="#3f8f1c"/>
    <rect x="128" y="955" width="196" height="70" fill="url(#cyl)"/>
    <ellipse cx="226" cy="955" rx="98" ry="18" fill="#b8ec4a"/>
    <text x="226" y="1000" text-anchor="middle" font-weight="900" font-size="18" fill="#fff">蓄積した監査ログ</text>

    <ellipse cx="666" cy="1025" rx="98" ry="18" fill="#3f8f1c"/>
    <rect x="568" y="955" width="196" height="70" fill="url(#cyl)"/>
    <ellipse cx="666" cy="955" rx="98" ry="18" fill="#b8ec4a"/>
    <text x="666" y="1000" text-anchor="middle" font-weight="900" font-size="18" fill="#fff">監査ポリシー</text>

    <ellipse cx="445" cy="985" rx="86" ry="36" fill="url(#pill)"/>
    <text x="445" y="992" text-anchor="middle" font-weight="900" font-size="18" fill="#fff">自動チェック</text>

    <path d="M355 985 L335 975 L335 995 Z" fill="#fff"/>
    <path d="M535 985 L555 975 L555 995 Z" fill="#fff"/>
    <line x1="325" y1="985" x2="340" y2="985" stroke="#fff" stroke-width="4"/>
    <line x1="550" y1="985" x2="568" y2="985" stroke="#fff" stroke-width="4"/>

    <path d="M445 1022 L445 1045" stroke="#d6141c" stroke-width="6"/>
    <path d="M255 1075 L300 1045 L590 1045 L635 1075 L590 1105 L300 1105 Z" fill="#d6141c"/>
    <text x="445" y="1083" text-anchor="middle" font-weight="900" font-size="21" fill="#fff">ポリシー違反検知</text>

    <path d="M200 1060 L200 1110 L182 1110 L212 1135 L242 1110 L224 1110 L224 1075 Z" fill="#d6141c"/>
    <path d="M690 1060 L690 1110 L708 1110 L678 1135 L648 1110 L666 1110 L666 1075 Z" fill="#d6141c"/>

    <text x="212" y="1165" text-anchor="middle" font-weight="900" font-size="20" fill="#fff">システム管理者へ警告</text>
    <text x="678" y="1165" text-anchor="middle" font-weight="900" font-size="20" fill="#fff">操作者へ警告</text>
  </svg>
</main>
</body>
</html>
```